Dream Enhancing Device - Comfortable & Sweet

Hello,

We want a website that SCREAMS comfort, dream, night, sweetness...

Something that, when you look at it, feels good.

Our website is about a device that helps you make you do beautiful dreams.

So, on the landing page, one must see the a picture of the device (see attached), with description, and everything must look profesional and comfortable

Be creative.

Need :
Landing page (home)
Product page (images with descriptions)
Contact page

Coding

Coded - Design and coding required

Number of Pages Required

3 page

Font styles to use
Sans Serif

Colors
3276b5
0392cd
33a6d7
ffffff
f68d4d
b7a5cd
876aae

Requirements
Must have
• Must look comfortable, feel like something sweet
Nice to have
• You can use clouds, moons, stars, anythings, be creative...

```html
<!DOCTYPE html>
<html lang="en">
<head>
<meta charset="utf-8">
<title>SomnaBand</title>
<link rel="stylesheet" href="https://fonts.googleapis.com/css2?family=Lato:wght@400;700;900&family=Open+Sans:ital,wght@0,400;0,600;0,700;1,400&display=swap">
<style>
:root{
  --blue-deep:#3276b5;
  --blue:#0392cd;
  --blue-light:#33a6d7;
  --white:#ffffff;
  --orange:#f68d4d;
  --lilac:#b7a5cd;
  --purple:#876aae;
  --ink:#1d1d1d;
  --text:#444;
  --grey-band:#bdbcbd;
  --footer:#2f5fa4;
}
*{margin:0;padding:0;box-sizing:border-box}
html,body{width:1200px;height:3516px;overflow:hidden}
body{position:relative;background:var(--white);font-family:"Open Sans",Arial,sans-serif;color:var(--text)}
.abs{position:absolute}
h1,h2,h3{font-family:"Lato",Arial,sans-serif;font-weight:400}

/* header */
.site-header{left:0;top:0;width:1200px;height:142px;background:var(--white);z-index:3}
.brand{left:108px;top:46px;display:flex;align-items:center;gap:10px;font-family:"Lato",sans-serif;font-weight:700;font-size:26px;color:var(--blue-deep);letter-spacing:.5px}
.brand-dot{width:34px;height:34px;border-radius:50%;background:var(--blue-deep)}
.main-nav{left:475px;top:60px;display:flex;gap:32px;font-family:"Lato",sans-serif;font-weight:700;font-size:16px;color:#222}
.main-nav .active{color:var(--blue)}

/* hero */
.hero{left:0;top:142px;width:1200px;height:614px;background:linear-gradient(100deg,#6a4ca2 0%,#4f62b6 30%,#2f7fc7 60%,#1f87cc 100%);overflow:hidden;z-index:2}
.hero-cloud{left:0;top:0}
.hero-title{left:516px;top:160px;color:var(--white);font-size:54px;letter-spacing:1px}
.hero-title b{font-weight:900}
.hero-sub{left:518px;top:250px;color:var(--white);font-family:"Open Sans",sans-serif;font-weight:600;font-size:26px;letter-spacing:2px;line-height:40px}
.hero-mouse{left:584px;top:462px}
.hero-band{left:760px;top:450px;width:400px;height:130px;border-radius:60px;background:linear-gradient(180deg,#3a3a3a,#151515)}

/* features */
.features{left:0;top:756px;width:1200px;height:860px;background:var(--grey-band);z-index:1}
.ghost{font-family:"Lato",sans-serif;font-weight:900;color:rgba(255,255,255,.25);white-space:nowrap;text-transform:uppercase}
.features .ghost{left:175px;top:96px;font-size:84px;color:rgba(0,0,0,.07)}
.section-title{font-size:44px;color:var(--ink);text-transform:uppercase;white-space:nowrap}
.section-title b{font-weight:900}
.features .section-title{left:0;width:1200px;text-align:center;top:108px}
.features .lead{left:0;width:1200px;text-align:center;top:200px;font-size:15px;color:#222}
.feat-label{font-family:"Lato",sans-serif;font-size:21px;color:var(--blue);display:flex;align-items:center;gap:12px}
.feat-note{font-size:14px;color:#222;white-space:nowrap}
.feat-line{border-top:1px dashed #7a7a7a}
.feat-v{border-left:1px dashed #7a7a7a}
.feature-device{left:410px;top:300px;width:390px;height:250px;border-radius:50%;background:radial-gradient(ellipse at 50% 45%,#d8d8d8 0 38%,#2a2a2a 40% 100%)}

/* about */
.about{left:0;top:1470px;width:1200px;height:580px;z-index:4}
.about .ghost{left:1120px;top:80px;font-size:72px;writing-mode:vertical-rl;color:rgba(255,255,255,.12)}
.about-image{left:95px;top:120px;width:410px;height:290px;border-radius:40px;background:linear-gradient(135deg,#2b2b2b,#5a8fa8 45%,#b58fb0 70%,#2b2b2b)}
.about .section-title{left:566px;top:120px;color:var(--white);font-size:44px}
.about-text{left:566px;top:200px;width:523px;font-size:15px;line-height:29px;color:var(--white)}
.btn-outline{left:566px;top:390px;width:166px;height:50px;border:2px solid var(--white);border-radius:25px;color:var(--white);font-family:"Lato",sans-serif;font-weight:700;font-size:16px;display:flex;align-items:center;justify-content:center;gap:6px}

/* reviews */
.reviews-bg{left:0;top:1990px;width:1200px;height:1160px;background:linear-gradient(180deg,#f4f4f5 0%,#fafafa 40%,#f2f2f3 100%);z-index:0}
.reviews .ghost{left:0;width:1200px;text-align:center;top:2110px;font-size:92px;color:rgba(0,0,0,.06)}
.reviews .section-title{left:0;width:1200px;text-align:center;top:2150px}
.review{width:330px}
.avatar{width:62px;height:62px;border-radius:50%;background:linear-gradient(135deg,#c9b7a7,#7a6a60)}
.stars{color:var(--orange);font-size:16px;letter-spacing:2px;position:absolute;left:86px;top:0}
.quote{position:absolute;left:86px;top:26px;width:244px;font-style:italic;font-size:12px;line-height:23px;color:#555}
.reviewer{position:absolute;left:0;top:134px;font-family:"Lato",sans-serif;font-weight:700;font-size:14px;color:#222}
.role{position:absolute;left:0;top:160px;font-size:12px;color:#555}
.arrow{font-size:22px;color:#555}
.divider{left:110px;top:2543px;width:980px;border-top:1px solid #ddd}

/* what we do */
.work .ghost{left:0;top:2588px;font-size:96px;color:rgba(0,0,0,.06)}
.work .section-title{left:110px;top:2630px;font-size:44px}
.work-text{left:110px;top:2712px;width:460px;font-size:15px;line-height:26px;color:#444;text-align:justify}
.work-text p{margin-bottom:26px}
.btn-solid{left:110px;top:2928px;width:170px;height:52px;border-radius:26px;background:var(--blue);color:var(--white);font-family:"Lato",sans-serif;font-weight:700;font-size:16px;display:flex;align-items:center;justify-content:center;gap:6px}
.video{left:628px;top:2660px;width:472px;height:300px;background:linear-gradient(135deg,#b9aea6,#e9e4de 50%,#8d8178)}
.video-frame{left:618px;top:2650px}

/* footer */
.footer{left:0;top:3140px;width:1200px;height:376px}
.footer-title{left:110px;top:3225px;font-size:26px;color:var(--white);font-weight:700}
.subscribe{left:110px;top:3274px;width:340px;height:50px;border:2px solid var(--white);background:var(--white);display:flex}
.subscribe span{flex:1;padding:13px 14px;font-size:15px;color:#777}
.subscribe b{width:106px;background:var(--purple);color:var(--white);font-size:14px;display:flex;align-items:center;justify-content:center}
.social{left:110px;top:3352px;display:flex;gap:14px}
.social i{width:18px;height:18px;border-radius:50%;background:var(--white);display:block}
.foot-links{left:508px;top:3225px;list-style:none;font-size:15px;color:var(--white);line-height:33px}
.foot-links li::before{content:"»";margin-right:12px}
.foot-contact{left:686px;top:3225px;list-style:none;font-size:15px;color:var(--white)}
.foot-contact li{height:33px;display:flex;align-items:center;gap:10px;margin-bottom:32px}
.foot-contact li:nth-child(2){margin-bottom:30px}
.foot-device{left:926px;top:3212px;width:180px;height:186px;border-radius:50%;background:radial-gradient(ellipse at 50% 45%,#8fc3bf 0 36%,#2a2a2a 40% 100%)}
.foot-rule{left:110px;top:3436px;width:980px;border-top:1px solid rgba(255,255,255,.4)}
.copyright{left:0;width:1200px;top:3470px;text-align:center;font-size:15px;color:var(--white)}
</style>
</head>
<body>

<header class="site-header abs">
  <div class="brand abs"><span class="brand-dot"></span>SomnaBand</div>
  <nav class="main-nav abs">
    <span class="active">HOME</span><span>ABOUT US</span><span>PRODUCTS</span><span>WHAT WE DO</span><span>CONTACT US</span>
    <svg width="16" height="16" viewBox="0 0 16 16"><circle cx="6.5" cy="6.5" r="5" fill="none" stroke="#222" stroke-width="2.2"/><line x1="10.5" y1="10.5" x2="15" y2="15" stroke="#222" stroke-width="2.5"/></svg>
  </nav>
</header>

<section class="hero abs" role="img" aria-label="Night sky with stars above a sleeping figure on a cloud">
  <svg class="hero-cloud abs" width="1200" height="614" viewBox="0 0 1200 614">
    <path d="M0 380 C80 340 180 360 260 400 C320 440 360 520 420 560 C600 640 900 590 1200 560 L1200 614 L0 614Z" fill="#bdbcbd"/>
  </svg>
  <h1 class="hero-title abs">SOMNA<b>BAND</b></h1>
  <p class="hero-sub abs">With SomnaBand, You'll Dream Like<br>Never Before.</p>
  <svg class="hero-mouse abs" width="32" height="70" viewBox="0 0 32 70"><rect x="2" y="2" width="28" height="42" rx="14" fill="none" stroke="#fff" stroke-width="2.5"/><line x1="16" y1="10" x2="16" y2="20" stroke="#fff" stroke-width="2.5"/><path d="M16 50 V66 M10 60 L16 66 L22 60" fill="none" stroke="#fff" stroke-width="2.5"/></svg>
  <div class="hero-band abs" role="img" aria-label="Black dream band product"></div>
</section>

<section class="features abs">
  <div class="ghost abs">Product Features</div>
  <h2 class="section-title abs">Product <b>Features</b></h2>
  <p class="lead abs">Lorem ipsum dolor sit amet consectetur adipiscing elit eiusmod tempor incididunt ut dolore magna aliqua.</p>

  <div class="feat-label abs" style="left:128px;top:262px"><svg width="26" height="40" viewBox="0 0 26 40"><rect x="3" y="6" width="20" height="32" rx="2" fill="none" stroke="#0392cd" stroke-width="2"/><rect x="9" y="2" width="8" height="4" fill="#0392cd"/><path d="M15 12 L9 23 H14 L11 32 L18 20 H13Z" fill="#0392cd"/></svg>Battery</div>
  <div class="feat-v abs" style="left:166px;top:306px;height:24px"></div>
  <div class="feat-line abs" style="left:166px;top:330px;width:260px"></div>
  <div class="feat-note abs" style="left:166px;top:340px">Lasts Up To Served Week</div>

  <div class="feat-label abs" style="left:112px;top:408px"><svg width="36" height="36" viewBox="0 0 36 36"><path d="M10 30 C6 26 6 20 10 16 C10 8 16 4 22 4 C28 4 32 9 32 15 C32 21 26 22 26 28 C26 32 22 34 18 32" fill="none" stroke="#0392cd" stroke-width="2"/></svg>Hear</div>
  <div class="feat-note abs" style="left:166px;top:454px">Silent, Vibrating Alarm</div>

  <div class="feat-line abs" style="left:166px;top:540px;width:260px"></div>
  <div class="feat-note abs" style="left:166px;top:516px">Discreet &amp; Fully Adjustable Band</div>
  <div class="feat-v abs" style="left:166px;top:540px;height:34px"></div>
  <div class="feat-label abs" style="left:118px;top:574px"><svg width="34" height="40" viewBox="0 0 34 40"><circle cx="17" cy="14" r="11" fill="none" stroke="#0392cd" stroke-width="2"/><circle cx="17" cy="14" r="6" fill="none" stroke="#0392cd" stroke-width="2"/><path d="M17 14 V36" stroke="#0392cd" stroke-width="2.5"/></svg>Touch</div>

  <div class="feat-label abs" style="left:985px;top:262px">Learn<svg width="40" height="40" viewBox="0 0 40 40"><circle cx="20" cy="20" r="14" fill="none" stroke="#0392cd" stroke-width="2"/><circle cx="20" cy="20" r="6" fill="none" stroke="#0392cd" stroke-width="2"/></svg></div>
  <div class="feat-v abs" style="left:1032px;top:306px;height:24px"></div>
  <div class="feat-line abs" style="left:780px;top:330px;width:252px"></div>
  <div class="feat-note abs" style="left:808px;top:340px">SoftPulse Conditioning Technology</div>

  <div class="feat-label abs" style="left:980px;top:408px">Sense<svg width="40" height="40" viewBox="0 0 40 40"><circle cx="18" cy="13" r="7" fill="none" stroke="#0392cd" stroke-width="2"/><path d="M5 38 C5 26 31 26 31 38" fill="none" stroke="#0392cd" stroke-width="2"/></svg></div>
  <div class="feat-note abs" style="left:874px;top:454px">Biosensor Records Vitals</div>

  <div class="feat-line abs" style="left:780px;top:540px;width:252px"></div>
  <div class="feat-note abs" style="left:962px;top:516px">Easy to Use</div>
  <div class="feat-v abs" style="left:1032px;top:540px;height:34px"></div>
  <div class="feat-label abs" style="left:962px;top:574px">Reviews<svg width="40" height="40" viewBox="0 0 40 40"><circle cx="10" cy="16" r="5" fill="none" stroke="#0392cd" stroke-width="2"/><circle cx="30" cy="16" r="5" fill="none" stroke="#0392cd" stroke-width="2"/><rect x="4" y="26" width="32" height="10" fill="none" stroke="#0392cd" stroke-width="2"/></svg></div>

  <div class="feature-device abs" role="img" aria-label="Dream band shown at an angle with white inner lining"></div>
</section>

<div class="reviews-bg abs" role="img" aria-label="Soft faded photo of a person sleeping in white bedding"></div>

<section class="about abs">
  <svg class="abs" style="left:0;top:0" width="1200" height="580" viewBox="0 0 1200 580">
    <defs><linearGradient id="aboutGrad" x1="0" y1="0" x2="1" y2="1"><stop offset="0" stop-color="#3276b5"/><stop offset=".5" stop-color="#0392cd"/><stop offset="1" stop-color="#3276b5"/></linearGradient></defs>
    <path d="M0 70 Q600 -20 1200 70 L1200 510 Q600 600 0 510Z" fill="url(#aboutGrad)"/>
  </svg>
  <div class="ghost abs">About Us</div>
  <div class="about-image abs" role="img" aria-label="Two dream bands in blue and pink"></div>
  <h2 class="section-title abs">About <b>SomnaBand</b></h2>
  <p class="about-text abs">Lorem ipsum dolor sit amet, consectetur adipiscing elit, sed do eiusmod tempor incididunt ut labore et dolore magna aliqua. Ut enim ad minim veniam, quis nos trud exercitation ullamco laboris nisi ut aliquip ex ea commodo consequat. Duis aute irure dolor in reprehenderit in voluptate velit esse cillum dolore eu fugiat nulla pariatur. Excepteur sint occaecat cupidatat non proident.</p>
  <div class="btn-outline abs">BUY NOW <span>➔</span></div>
</section>

<section class="reviews">
  <div class="ghost abs">Client Reviews</div>
  <h2 class="section-title abs">Client <b>Reviews</b></h2>
  <span class="arrow abs" style="left:42px;top:2330px">‹</span>
  <span class="arrow abs" style="left:1142px;top:2330px">›</span>

  <article class="review abs" style="left:110px;top:2262px">
    <div class="avatar" role="img" aria-label="Reviewer portrait"></div>
    <div class="stars">★★★★☆</div>
    <p class="quote">“ At vero eos et accusamus et iustodio dignissimos ducimus qui blanditiispraesent ium voluptatum deleniti atque corrupti quos dolores quas molestias ”</p>
    <div class="reviewer">LENA MARSH</div>
    <div class="role">Creative Manager, USA</div>
  </article>
  <article class="review abs" style="left:450px;top:2262px">
    <div class="avatar" role="img" aria-label="Reviewer portrait"></div>
    <div class="stars">★★★★☆</div>
    <p class="quote">“ At vero eos et accusamus et iustodio dignissimos ducimus qui blanditiispraesent ium voluptatum deleniti atque corrupti quos dolores quas molestias ”</p>
    <div class="reviewer">OWEN PIKE</div>
    <div class="role">Events Manager, USA</div>
  </article>
  <article class="review abs" style="left:790px;top:2262px">
    <div class="avatar" role="img" aria-label="Reviewer portrait"></div>
    <div class="stars">★★★★☆</div>
    <p class="quote">“ At vero eos et accusamus et iustodio dignissimos ducimus qui blanditiispraesent ium voluptatum deleniti atque corrupti quos dolores quas molestias ”</p>
    <div class="reviewer">THEO VANCE</div>
    <div class="role">Task Manager, USA</div>
  </article>
</section>

<div class="divider abs"></div>

<section class="work">
  <div class="ghost abs">What We Do</div>
  <h2 class="section-title abs">What <b>We Do</b></h2>
  <div class="work-text abs">
    <p>Lorem ipsum dolor sit amet, consectetur adipiscing elit, sed do eiusmod tempor incididunt ut labore et dolore magna aliqua.</p>
    <p>Ut enim ad minim veniam, quis nostrud exercitation ullamco laboris nisi ut aliquip ex ea commodo consequat. Duis aute irure dolor in reprehenderit in voluptate velit esse cillum dolore eu fugiat nulla pariatur. Excepteur sint occaecat cupidatat.</p>
  </div>
  <div class="btn-solid abs">READ MORE <span>➔</span></div>
  <div class="video abs" role="img" aria-label="Video still of a woman asleep wearing the dream band"></div>
  <svg class="video-frame abs" width="494" height="322" viewBox="0 0 494 322">
    <path d="M2 30 V2 H30 M464 2 H492 V30 M492 292 V320 H464 M30 320 H2 V292" fill="none" stroke="#876aae" stroke-width="4"/>
    <circle cx="247" cy="158" r="26" fill="#ffffff" fill-opacity=".85"/>
    <path d="M240 146 L259 158 L240 170Z" fill="#876aae"/>
  </svg>
</section>

<footer class="footer abs">
  <svg class="abs" style="left:0;top:0" width="1200" height="376" viewBox="0 0 1200 376">
    <path d="M0 40 Q600 -30 1200 40 L1200 376 L0 376Z" fill="#2f5fa4"/>
  </svg>
</footer>
<h3 class="footer-title abs">Stay Updated</h3>
<div class="subscribe abs"><span>Email Address</span><b>SUBSCRIBE</b></div>
<div class="social abs"><i></i><i></i><i></i><i></i><i></i></div>
<ul class="foot-links abs"><li>Home</li><li>About Us</li><li>Products</li><li>Our Technology</li><li>Contact Us</li></ul>
<ul class="foot-contact abs">
  <li><svg width="16" height="12" viewBox="0 0 16 12"><rect x="1" y="1" width="14" height="10" fill="none" stroke="#fff" stroke-width="1.5"/><path d="M1 1 L8 7 L15 1" fill="none" stroke="#fff" stroke-width="1.5"/></svg>hello@somnaband.com</li>
  <li><svg width="14" height="14" viewBox="0 0 14 14"><path d="M3 1 L5 4 L4 6 C5 8 6 9 8 10 L10 9 L13 11 L11 13 C6 13 1 8 1 3Z" fill="#fff"/></svg>(+1) 555 014 2290</li>
  <li><svg width="12" height="16" viewBox="0 0 12 16"><path d="M6 15 C2 10 1 8 1 6 A5 5 0 0 1 11 6 C11 8 10 10 6 15Z" fill="#fff"/><circle cx="6" cy="6" r="2" fill="#2f5fa4"/></svg>48 Willow Lane, US</li>
</ul>
<div class="foot-device abs" role="img" aria-label="Dream band with mint inner lining"></div>
<div class="foot-rule abs"></div>
<p class="copyright abs">© Copyright 2019 SomnaBand. All Rights Reserved &nbsp;|&nbsp; Privacy Policy.</p>

</body>
</html>
```